NOTE: I PROVIDED THE INCORRECT LOGO AND ONLY A HANDFUL OF PEOPLE NOTICED THAT IT WAS NOT THE ONE I DESCRIBED. THE LOGO I HAVE NOW ATTACHED MATCHES MY WEBSITE AND THE COLORS ON THE WEBSITE SHOULD BE USED FOR THE CARD.

PLEASE READ THE BUSINESS CARD DETAILS AND PROJECT MUST HAVES CAREFULLY.

I am looking for a business card that is powerful, a bit edgy, and although I work in the corporate world, not too formal. I would like to see designs that use the colors on my website www.brightmoorlane.com. I don't want the card to look washed out so please use shades of those colors that make them "pop". The "vibe" of the card needs to show substance and confidence while also reflecting that we're not your usual consultants.

The focus of my work is turning "people problems" into profits. Those problems could be poor service, an unstable workforce, untrained leaders, or managing change. We are an aggressive, results-focused team of performance improvement professionals who refuse to believe "things can't be done". For us, failure is not an option. Our logo reflects a target from the view of the site on a gun.

In addition to the contact information provided on the sample business card (do not include "turning people problems into profits"), I would like to include this statement (probably on the back):
I equip results-oriented business leaders to turn their people problems into profits in six months or less.

PLEASE NOTE THAT MY WEBSITE IS UNDER REVISION TO TONE DOWN THE MILITARY THEME, ALTHOUGH THE WARRIOR ENERGY AND FOCUS ON RESULTS REMAINS.

Target Market(s)

My clients are Mid and senior-level managers. I don't target any particular industry.

Industry/Entity Type

Consulting

Contact Information for Business Card

In addition to the contact information provided on the sample business card (DO NOT INCLUDE "turning people problems into profits"), I would like to include this statement (probably on the back):

I don't care whether the card is landscape or portrait view.

Font styles to use
Sans Serif

Requirements
Must have
• 1. be easy to read, no 6-8 point fonts!
• 2. a "vibe" that captures the eye without being too chaotic or busy
• 3. bold color, not washed out or boring - a good blend with the colors currently on my website (black, red, white, army green) but you don't need to use all of them.
• 4. all the contact information I have provided
• 5. a good blend with the colors currently on my website
• 6. Must have this quote on the back of the card: I equip results-oriented business leaders to turn their people problems into profits in six months or less.
Nice to have
• In looking at the sample images I provided for ideas, you can see that I like the way a card carries over from one side to the next.
• It would be great to find some aspect/quality/feature that I haven't seen before
Should not have
• 1. NO use of ALL CAPS
• 2. fonts that I would have to seek out and purchase (you should provide files for font if using something not standard)

```html
<!DOCTYPE html>
<html lang="en">
<head>
<meta charset="utf-8">
<title>Brightmoor Lane Inc — Business Card</title>
<link rel="stylesheet" href="https://fonts.googleapis.com/css2?family=Graduate&family=Roboto+Condensed:wght@400;500&family=Questrial&display=swap">
<style>
  :root {
    --backdrop: #1b1b1b;
    --card-back: #262626;
    --card-front: #0c0c0c;
    --lime: #9fd03c;
    --white: #ffffff;
    --sky: #4ab3e6;
    --steel-blue: #3e6f9a;
    --forest: #2f6b46;
  }
  * { margin: 0; padding: 0; box-sizing: border-box; }
  html, body { width: 1200px; height: 1200px; overflow: hidden; background: var(--backdrop); }
  .canvas {
    width: 1200px; height: 1200px;
    display: flex; flex-direction: column; align-items: center; justify-content: center; gap: 44px;
  }
  .card { width: 900px; height: 514px; position: relative; overflow: hidden; box-shadow: 0 10px 30px rgba(0,0,0,.5); }

  /* Back side */
  .card--back { background: var(--card-back); }
  .mission {
    position: absolute; left: 70px; top: 92px; width: 560px;
    font-family: "Graduate", serif; font-size: 33px; line-height: 1.42;
    text-transform: uppercase; color: var(--white); letter-spacing: .5px;
  }
  .mission .accent { color: var(--lime); }
  .stripe { position: absolute; left: 664px; top: 0; width: 22px; height: 100%; display: flex; flex-direction: column; }
  .stripe span { display: block; }
  .stripe .s1 { height: 16%; background: var(--steel-blue); }
  .stripe .s2 { height: 34%; background: var(--lime); }
  .stripe .s3 { height: 20%; background: var(--sky); }
  .stripe .s4 { height: 30%; background: var(--forest); }
  .brand-panel { position: absolute; left: 686px; top: 0; width: 214px; height: 100%; background: var(--lime); }
  .brand-panel__name {
    position: absolute; left: 50%; top: 50%;
    transform: translate(-50%, -50%) rotate(-90deg);
    font-family: "Questrial", sans-serif; font-size: 46px; color: var(--white); white-space: nowrap;
    display: flex; align-items: center; gap: 16px;
  }
  .brand-panel__mark { width: 22px; height: 22px; background: var(--white); }

  /* Front side */
  .card--front { background: var(--card-front); font-family: "Roboto Condensed", sans-serif; }
  .front-brand {
    position: absolute; right: 70px; top: 64px;
    font-family: "Roboto Condensed", sans-serif; font-weight: 400; font-size: 62px; color: var(--lime);
  }
  .contact { position: absolute; left: 70px; right: 70px; top: 218px; }
  .contact__row { display: flex; align-items: baseline; justify-content: space-between; }
  .contact__name { font-size: 52px; font-weight: 500; color: var(--white); text-transform: uppercase; }
  .contact__title { font-size: 28px; color: var(--lime); text-transform: uppercase; }
  .rule { height: 2px; background: var(--sky); margin: 10px 0 12px; }
  .phone { font-size: 40px; color: var(--white); }
  .phone .label { font-size: 28px; color: var(--lime); text-transform: uppercase; }
  .web-row { font-size: 29px; color: var(--white); text-transform: uppercase; letter-spacing: .5px; }
</style>
</head>
<body>
<main class="canvas">
  <section class="card card--back">
    <p class="mission">I equip results oriented <span class="accent">business leaders</span> to turn their <span class="accent">people problems</span> into profits in <span class="accent">six months</span> or <span class="accent">less.</span></p>
    <div class="stripe"><span class="s1"></span><span class="s2"></span><span class="s3"></span><span class="s4"></span></div>
    <div class="brand-panel">
      <div class="brand-panel__name"><span class="brand-panel__mark"></span>Brightmoor Lane Inc</div>
    </div>
  </section>

  <section class="card card--front">
    <div class="front-brand">Brightmoor Lane Inc</div>
    <div class="contact">
      <div class="contact__row">
        <span class="contact__name">Dana Whitcombe</span>
        <span class="contact__title">Chief Performance Strategist</span>
      </div>
      <div class="rule"></div>
      <div class="contact__row">
        <span class="phone"><span class="label">Phone:</span> 248-555-0142</span>
        <span class="phone"><span class="label">Mobile:</span> 248-555-0187</span>
      </div>
      <div class="rule"></div>
      <div class="web-row">dana@brightmoorlane.com &nbsp;|&nbsp; www.brightmoorlane.com</div>
    </div>
  </section>
</main>
</body>
</html>
```